Web Design / Transformation our Joomla web site

Job Type
We are looking for a fresh eye-catching Custom Joomla Design to transform our Joomla web site

Task Description
We are in a process to create web site to Speech Pathology services . The site is built by using brightframe ((http://www.brightframe-example.com/) horizon template.

You can see our site http://pebblelanetherapy-example.com/demo

Unfortunately, this template does not match our identity. We would like to improve or replace it. Although we like features that brightframe template is giving as part of their template ,we want to transform our site to something more simplistic and kids oriented . We don’t like look and fill of our website since it’s very professional and “corporate” . Our business is very small and is not 100 people company , we are looking for something more simple and personal. It should look professional, all be it, child friendly. We work on children’s communication skills, and we want to convey an idea that communication is “Pebble Lane”, meaning children need to learn to play and socialize appropriately. In addition, learning to be a better communicators will help them to be closer to their family members and friends. We want our website to show kids playing and having fun. In other hand , we don't want the Website to be too busy with images, so use your professional judgment.
You can change current template or you can provide your own Joomla design.

Examples of website look that we like :

http://sunnygablestherapy-example.com
http://thetalkinggardeners-example.com/
http://rowanvoiceclinic-example.com/

About Our Company :
Company name: Pebble Lane
What we do: Pediatric Speech & Language Pathology Services. We established Pebble Lane to provide families with a unique option for their child’s speech therapy needs. Our clinic is founded on the principle that all children are different and require a thoughtful, parent-driven therapy plan. When a family chooses us, they will enter a partnership with an experienced, well-trained therapist.
Top Three Things to Communicate through our Website:
#1 - We are kids friendly
#2 - We are professional
#3 - We provide our services with a loving, nurturing attitude toward the child and with compassionate, comprehensive support and input for the family
Updates

To see current running site : http://pebblelanetherapy-example.com/demo/

Reason: There are no good designs to address our needs

Reason: It's still work in progress. Submitted designs are still under constructions and waiting for updates

We are accepting WordPress designs as well !!!

Target Market(s)

Families with kids

Industry/Entity Type

Communication

Requirements
Must have
• • Joomla/Wordpress as a platform
• Easy to Navigate
• Clean Design, kids friendly but professional

```html
<!DOCTYPE html>
<html lang="en">
<head>
<meta charset="utf-8">
<title>Pebble Lane – Speech &amp; Language Pathology Services</title>
<link href="https://fonts.googleapis.com/css2?family=Fenix&family=Open+Sans:wght@400;600&family=Oswald:wght@400&display=swap" rel="stylesheet">
<style>
:root{
  --sky-top:#8fcdf3;
  --sky-bottom:#e6f4fc;
  --nav-top:#3ec3f3;
  --nav-bottom:#0a9ee0;
  --nav-line:#7fd6f6;
  --red:#d7141d;
  --blue:#1a93cf;
  --green:#5f9e1f;
  --text:#6b6b6b;
  --heading:#4a4a4a;
  --sunflower:#f7c51d;
  --footer:#3f7d1b;
  --white:#ffffff;
}
*{box-sizing:border-box;margin:0;padding:0}
html,body{width:710px;height:1200px;overflow:hidden;background:var(--white)}
body{font-family:"Open Sans",Arial,sans-serif;color:var(--text)}
.page{position:relative;width:710px;height:1200px;overflow:hidden;
  background:linear-gradient(to bottom,var(--sky-top) 0,var(--sky-bottom) 260px,var(--white) 400px,var(--white) 100%)}
a{color:inherit;text-decoration:none}

/* header */
.brand{position:absolute;left:58px;top:20px;width:200px}
.brand-name{display:flex;align-items:center;gap:6px;font-family:"Fenix",Georgia,serif;font-size:24px;line-height:1.1;color:var(--red);white-space:nowrap}
.brand-mark{width:14px;height:14px;border-radius:50%;background:var(--sunflower);flex:none}
.brand-tag{margin-top:40px;font-size:5.5px;font-weight:600;color:#2a5aa8;letter-spacing:.1px}
.search{position:absolute;left:491px;top:75px;width:163px;height:20px;background:var(--white);border:1px solid #cfdce4;border-radius:2px;
  display:flex;align-items:center;justify-content:space-between;padding:0 6px 0 8px;font-size:7px;font-style:italic;color:#9a9a9a}

.nav{position:absolute;left:55px;top:105px;width:600px;height:30px;display:flex;
  background:linear-gradient(to bottom,var(--nav-top),var(--nav-bottom))}
.nav a{display:flex;align-items:center;justify-content:center;font-family:"Oswald",Arial,sans-serif;font-size:10.5px;color:var(--white);border-right:1px solid var(--nav-line);letter-spacing:.2px}
.nav a:last-child{border-right:0}

/* scenery */
.field-left,.field-right{position:absolute;top:140px;height:240px;
  background:linear-gradient(to bottom,rgba(185,224,122,0),#b9e07a 18%,#f3d35a 45%,#e9c237 62%,#9fcf58 85%,rgba(255,255,255,0))}
.field-left{left:0;width:56px}
.field-right{left:652px;width:58px}
.field-strip{position:absolute;left:0;top:310px;width:710px;height:90px;
  background:linear-gradient(to bottom,rgba(185,224,122,0),rgba(170,214,100,.55) 30%,rgba(255,232,140,.5) 60%,rgba(255,255,255,0))}

/* hero */
.hero{position:absolute;left:55px;top:135px;width:598px;height:220px}
.hero svg.panel{position:absolute;left:0;top:0}
.hero-copy{position:absolute;left:41px;top:43px;width:240px}
.hero-title{font-family:"Fenix",Georgia,serif;font-weight:400;font-size:22px;line-height:25px;color:var(--red)}
.hero-text{margin-top:4px;font-size:7.2px;line-height:11.5px;color:var(--blue)}
.btn{display:inline-block;margin-top:9px;width:61px;height:19px;line-height:19px;text-align:center;border-radius:2px;
  background:linear-gradient(to bottom,#8dc73f,#5d9e1f);color:var(--white);font-family:"Oswald",Arial,sans-serif;font-size:7px}
.slider-arrows{position:absolute;left:43px;top:167px}
.hero-photo{position:absolute;left:309px;top:13px;width:276px;height:182px;border:4px solid var(--white);box-shadow:0 1px 4px rgba(0,0,0,.2);
  background:linear-gradient(135deg,#cfd9c2,#e9c8a4 45%,#d77a3e 80%,#b84835)}

/* posts */
.posts{position:absolute;left:58px;top:390px;width:382px}
.post{padding-bottom:14px;margin-bottom:16px;border-bottom:1px dotted #8a8a8a}
.post:last-child{border-bottom:0}
.post-title{font-family:"Fenix",Georgia,serif;font-weight:400;font-size:14.5px;color:var(--heading);margin-bottom:6px}
.post p{font-size:7.3px;line-height:12.8px;margin-bottom:5px}
.post-meta{margin-top:10px;font-size:7.3px;color:var(--red)}
.post-meta span{margin:0 4px}

/* sidebar */
.sidebar{position:absolute;left:467px;top:388px;width:162px;height:640px;border-left:1px solid #e2e2e2;padding-left:15px}
.widget{padding-bottom:12px;margin-bottom:14px;border-bottom:1px solid #d8d8d8}
.widget:last-child{border-bottom:0}
.widget-title{font-family:"Fenix",Georgia,serif;font-weight:400;font-size:14px;margin-bottom:6px}
.widget-title.red{color:var(--red)}
.widget-title.blue{color:var(--blue)}
.widget-title.green{color:var(--green)}
.arrow-list{list-style:none}
.arrow-list li{position:relative;padding-left:11px;font-size:7.2px;line-height:17.6px;color:#555}
.arrow-list li::before{content:"";position:absolute;left:2px;top:6px;border-left:3px solid #888;border-top:2.5px solid transparent;border-bottom:2.5px solid transparent}
.arrow-list.archive li{color:var(--green)}
.popular{list-style:none}
.popular li{font-size:7.1px;line-height:11.5px;color:#777;padding:5px 0;border-bottom:1px solid #e4e4e4}
.popular li:last-child{border-bottom:0}

/* footer */
.footer-field{position:absolute;left:0;top:1036px;width:710px;height:86px;
  background:linear-gradient(to bottom,rgba(255,255,255,0),#ffe487 25%,#f5b81a 55%,#8fb43a 85%,var(--footer))}
.footer{position:absolute;left:0;top:1120px;width:710px;height:80px;background:var(--footer)}
.footer-nav{position:absolute;left:58px;top:25px;font-size:8.3px;color:var(--white)}
.footer-nav span{margin:0 5px;color:var(--white)}
.copyright{position:absolute;left:58px;top:43px;font-size:6.5px;color:#b8d39c}
.social{position:absolute;left:567px;top:27px;display:flex;gap:4px}
.social i{display:block;width:18px;height:18px;border-radius:50%;background:var(--white)}
</style>
</head>
<body>
<div class="page">

  <div class="field-left" role="img" aria-label="Sunflowers and trees beside the meadow"></div>
  <div class="field-right" role="img" aria-label="Sunflowers and trees beside the meadow"></div>
  <div class="field-strip" role="img" aria-label="Grassy meadow with sunflowers"></div>

  <header>
    <a class="brand" href="#">
      <div class="brand-name"><span class="brand-mark"></span>Pebble Lane</div>
      <div class="brand-tag">Speech &amp; Language Pathology Services</div>
    </a>
    <div class="search">Search here
      <svg width="10" height="10" viewBox="0 0 10 10"><circle cx="4.2" cy="4.2" r="3.2" fill="none" stroke="#888" stroke-width="1.2"/><line x1="6.6" y1="6.6" x2="9.3" y2="9.3" stroke="#888" stroke-width="1.3"/></svg>
    </div>
    <nav class="nav">
      <a href="#" style="width:61px">HOME</a>
      <a href="#" style="width:70px">ABOUT US</a>
      <a href="#" style="width:138px">TREATMENT TECHNIQUES</a>
      <a href="#" style="width:90px">RECENT BLOG</a>
      <a href="#" style="width:45px">FAQ</a>
      <a href="#" style="width:81px">RESOURCES</a>
      <a href="#" style="width:70px">CONTACT</a>
    </nav>
  </header>

  <section class="hero">
    <svg class="panel" width="598" height="220" viewBox="0 0 598 220">
      <defs>
        <linearGradient id="panelFill" x1="0" y1="0" x2="0" y2="1">
          <stop offset="0" stop-color="#ffffff"/>
          <stop offset="1" stop-color="#e3f1fa"/>
        </linearGradient>
      </defs>
      <path d="M0 0H598V210C520 190 440 180 360 195C270 212 150 222 0 198Z" fill="url(#panelFill)"/>
    </svg>
    <div class="hero-copy">
      <h1 class="hero-title">Duis sed tellus et<br>Phasellus felis dolor</h1>
      <p class="hero-text">Mauris vel lacus vitae felis vestibulum volutpat. Etiam est nunc, venenatis in, tristique eu, imperdiet ac, nisl. Cum sociis natoque penatibus et magnis dis parturient montes</p>
      <a class="btn" href="#">LEARN MORE</a>
    </div>
    <svg class="slider-arrows" width="20" height="12" viewBox="0 0 20 12">
      <path d="M6 1L1 6L6 11M13 1L18 6L13 11" fill="none" stroke="#3a8fc8" stroke-width="1.4"/>
    </svg>
    <div class="hero-photo" role="img" aria-label="Teacher reading a picture book to a group of children in a classroom"></div>
  </section>

  <main class="posts">
    <article class="post">
      <h2 class="post-title">Nunc tempus felis vitae urna</h2>
      <p>Vivamus porttitor, g, purus nisi eleifend libero, a tempus libero lectus feugiat felis. Morbi diam mauris, viverra in, gravida eu, mattis in, ante. Morbi eget arcu. Morbi porta, libero id ullamcorper nonummy.</p>
      <p>Nibh ligula pulvinar metus, eget consectetuer augue nisi quis lacus. Ut ac mi quis lacus mollis aliquam. Curabitur iaculis tempus eros. Curabitur vel mi sit amet magna malesuada ultrices. Ut nisi erat, fermentum vel, congue id, euismod in, elit. Fusce ultricies, orci ac feugiat suscipit, leo massa sodales velit</p>
      <div class="post-meta">Learn More<span>|</span>2 Comments<span>|</span>Posted on June 15, 2013</div>
    </article>
    <article class="post">
      <h2 class="post-title">Phasellus felis dolor scelerisque tempus</h2>
      <p>Vivamus porttitor, g, purus nisi eleifend libero, a tempus libero lectus feugiat felis. Morbi diam mauris, viverra in, gravida eu, mattis in, ante. Morbi eget arcu. Morbi porta, libero id ullamcorper nonummy.</p>
      <p>Nibh ligula pulvinar metus, eget consectetuer augue nisi quis lacus. Ut ac mi quis lacus mollis aliquam. Curabitur iaculis tempus eros. Curabitur vel mi sit amet magna malesuada ultrices. Ut nisi erat, fermentum vel, congue id, euismod in, elit. Fusce ultricies, orci ac feugiat suscipit, leo massa sodales velit</p>
      <div class="post-meta">Learn More<span>|</span>2 Comments<span>|</span>Posted on June 15, 2013</div>
    </article>
    <article class="post">
      <h2 class="post-title">Duis sed tellus et tortor vestibulum gravida</h2>
      <p>Vivamus porttitor, g, purus nisi eleifend libero, a tempus libero lectus feugiat felis. Morbi diam mauris, viverra in, gravida eu, mattis in, ante. Morbi eget arcu. Morbi porta, libero id ullamcorper nonummy.</p>
      <p>Nibh ligula pulvinar metus, eget consectetuer augue nisi quis lacus. Ut ac mi quis lacus mollis aliquam</p>
      <div class="post-meta">Learn More<span>|</span>2 Comments<span>|</span>Posted on June 15, 2013</div>
    </article>
    <article class="post">
      <h2 class="post-title">Duis sed tellus et tortor vestibulum gravida</h2>
      <p>Vivamus porttitor, g, purus nisi eleifend libero, a tempus libero lectus feugiat felis. Morbi diam mauris, viverra in, gravida eu, mattis in, ante. Morbi eget arcu. Morbi porta, libero id ullamcorper nonummy.</p>
      <p>Nibh ligula pulvinar metus, eget consectetuer augue nisi quis lacus. Ut ac mi quis lacus mollis aliquam</p>
      <div class="post-meta">Learn More<span>|</span>2 Comments<span>|</span>Posted on June 15, 2013</div>
    </article>
    <article class="post">
      <h2 class="post-title">Curabitur vel mi sit amet magna malesuada</h2>
      <p>Vivamus porttitor, g, purus nisi eleifend libero, a tempus libero lectus feugiat felis. Morbi diam mauris, viverra in, gravida eu, mattis in, ante. Morbi eget arcu. Morbi porta, libero id ullamcorper nonummy.</p>
      <p>Nibh ligula pulvinar metus, eget consectetuer augue nisi quis lacus. Ut ac mi quis lacus mollis aliquam</p>
      <div class="post-meta">Learn More<span>|</span>2 Comments<span>|</span>Posted on June 15, 2013</div>
    </article>
  </main>

  <aside class="sidebar">
    <section class="widget">
      <h3 class="widget-title red">Our Category</h3>
      <ul class="arrow-list">
        <li>Duis tincidunt lectus</li>
        <li>Wuis dui viverra vestibulum.</li>
        <li>Suspendisse vulputate aliquam dui.</li>
        <li>Nulla elementum dui</li>
        <li>Aliquam vehicula</li>
        <li>Maecenas placerat</li>
        <li>Nisl at consequat</li>
        <li>Sem nunc gravida</li>
        <li>Justo quis eleifend arcu</li>
      </ul>
    </section>
    <section class="widget">
      <h3 class="widget-title blue">Popular Posts</h3>
      <ul class="popular">
        <li>Donec scelerisque leo ac risus. Praesent sit amet est in dictum dolor eu dictum</li>
        <li>Porttitor, enim felis viverra mi eget luctus</li>
        <li>Etiam nulla massa pharetra facilisis, volut-pat in imperdiet sit amet sem</li>
        <li>Aliquam nec erat at purus cursus interdum Vestibulum ligula</li>
      </ul>
    </section>
    <section class="widget">
      <h3 class="widget-title green">Blog Archive</h3>
      <ul class="arrow-list archive">
        <li>July 2012</li>
        <li>February 2012</li>
        <li>January 2012</li>
        <li>December 2011</li>
        <li>November 2011</li>
        <li>October 2011</li>
        <li>September 2011</li>
        <li>August 2011</li>
        <li>July 2011</li>
      </ul>
    </section>
  </aside>

  <div class="footer-field" role="img" aria-label="Row of sunflowers above the grass"></div>
  <footer class="footer">
    <nav class="footer-nav">HOME<span>|</span>ABOUT US<span>|</span>TREATMENT TECHNIQUES<span>|</span>RECENT BLOG<span>|</span>FAQ<span>|</span>RESOURCES<span>|</span>CONTACT</nav>
    <p class="copyright">Copyright © 2013 Company name.&nbsp; All right reserved</p>
    <div class="social" aria-label="Social links"><i></i><i></i><i></i><i></i></div>
  </footer>

</div>
</body>
</html>
```